We need a fresh, new church business card!!

We need a church business card with basic info to hand out as invites. We are looking for something clean that communicates our basic information clearly.

We are open to square or rectangle card sizes.

General Public

Religious

The attached logo is the only one that I have available. We'd like to see options with with text of the logo lighter and on a dark background as well as options with white/light backgrounds.

Also, we'd like to see option with rounded corners.

• Address - 2718 Maple Row, Rockford, IL 61142
• Website - brookvane.example
• Phone - 815-555-0163
• Service times -
• Sunday - 10am Sunday School
• - 11am Family Worship
• - 6pm Night of Prayer
• Wednesday - 7:30pm Adult Bible Study
• Classes for all ages

```html
<!DOCTYPE html>
<html lang="en">
<head>
<meta charset="utf-8">
<title>Brookvane Pentecostal Church – Service Card</title>
<link href="https://fonts.googleapis.com/css2?family=Open+Sans:wght@400;600;700&display=swap" rel="stylesheet">
<style>
  :root {
    --backdrop: #e4e4e2;
    --card-white: #f7f7f5;
    --card-dark: #2b2a2c;
    --teal: #4b8a98;
    --teal-text: #5a9aa8;
    --ink: #2a2a2c;
    --logo-grey: #6b6b6d;
    --light-text: #d6d6d6;
    --muted-text: #a9a9ab;
    --divider: #bdbdbd;
  }
  * { margin: 0; padding: 0; box-sizing: border-box; }
  html, body {
    width: 1200px; height: 800px; overflow: hidden;
    background: var(--backdrop);
    font-family: "Open Sans", sans-serif;
  }
  .card {
    position: absolute; left: 160px; top: 150px;
    width: 880px; height: 500px;
    border-radius: 36px; overflow: hidden;
    background: var(--card-dark);
    box-shadow: 0 6px 18px rgba(0,0,0,0.12);
  }
  .card__shapes { position: absolute; inset: 0; }
  .brand {
    position: absolute; top: 88px; left: 0; width: 100%;
    display: flex; justify-content: center; align-items: center; gap: 18px;
  }
  .brand__mark {
    width: 58px; height: 58px; border-radius: 50%; background: var(--teal);
  }
  .brand__name {
    font-weight: 600; font-size: 34px; color: var(--logo-grey);
    letter-spacing: 0.5px;
  }
  .band-title {
    position: absolute; top: 220px; left: 0; width: 100%;
    text-align: center; font-size: 36px; line-height: 1.3;
    color: var(--ink); font-weight: 400;
  }
  .band-title strong { font-weight: 700; }
  .schedule {
    position: absolute; top: 304px; text-align: center;
    color: var(--light-text); font-size: 24px; line-height: 1.3;
  }
  .schedule--wednesday { left: 40px; width: 380px; }
  .schedule--sunday { left: 460px; width: 380px; }
  .schedule__day { color: var(--teal-text); font-weight: 700; }
  .divider {
    position: absolute; left: 439px; top: 314px;
    width: 2px; height: 118px; background: var(--divider);
  }
  .contact {
    position: absolute; left: 0; top: 452px; width: 100%;
    display: flex; justify-content: center; gap: 34px;
    font-size: 16px; line-height: 20px; color: var(--muted-text);
  }
  .contact__item { display: flex; align-items: center; gap: 8px; white-space: nowrap; }
  .contact__icon { width: 16px; height: 16px; flex: none; }
</style>
</head>
<body>
  <div class="card">
    <svg class="card__shapes" width="880" height="500" viewBox="0 0 880 500" aria-hidden="true">
      <rect class="card__light-panel" x="0" y="0" width="880" height="197" fill="var(--card-white)"/>
      <path class="card__service-band"
            d="M0 196 L880 196 L880 200 Q852 204 852 236 L852 260 Q852 288 822 288 L58 288 Q28 288 28 260 L28 236 Q28 204 0 200 Z"
            fill="var(--teal)"/>
    </svg>

    <div class="brand">
      <span class="brand__mark"></span>
      <span class="brand__name">Brookvane Pentecostal Church</span>
    </div>

    <h1 class="band-title"><strong>Service</strong> times</h1>

    <div class="schedule schedule--wednesday">
      <div class="schedule__day">Wednesday</div>
      <div>7:30pm Adult Bible Study</div>
      <div>Classes for all ages</div>
    </div>

    <div class="divider"></div>

    <div class="schedule schedule--sunday">
      <div class="schedule__day">Sunday</div>
      <div>10am Sunday School</div>
      <div>11am Family Worship</div>
      <div>6pm Night of Prayer</div>
    </div>

    <div class="contact">
      <span class="contact__item">
        <svg class="contact__icon" viewBox="0 0 16 16" aria-hidden="true"><path d="M8 1a5 5 0 0 0-5 5c0 4 5 9 5 9s5-5 5-9a5 5 0 0 0-5-5zm0 7a2 2 0 1 1 0-4 2 2 0 0 1 0 4z" fill="var(--teal-text)"/></svg>
        2718 Maple Row, Rockford, IL 61142
      </span>
      <span class="contact__item">
        <svg class="contact__icon" viewBox="0 0 16 16" aria-hidden="true"><g fill="none" stroke="var(--teal-text)" stroke-width="1.4"><circle cx="8" cy="8" r="6.3"/><ellipse cx="8" cy="8" rx="2.8" ry="6.3"/><path d="M1.7 8h12.6"/></g></svg>
        brookvane.example
      </span>
      <span class="contact__item">
        <svg class="contact__icon" viewBox="0 0 16 16" aria-hidden="true"><path d="M4.2 1.5l2 3-1.3 1.6a8 8 0 0 0 5 5l1.6-1.3 3 2-1 2.4c-6 .3-11.6-5.3-11.3-11.3z" fill="var(--teal-text)"/></svg>
        815-555-0163
      </span>
    </div>
  </div>
</body>
</html>
```